Need a plumber

Would like a postcard sized flyer made up. Want the design to be kept very simple.
List of services we carry out in bullet point or similar.
Phone number and email included on the flyer.
Logo to feature prominantly.

List of services: Hot water issues
Burst Pipes
Gas Plumbing
Roof leaks
Drain blockages

Target Market(s)

Mums, dads and hosehgold owners

Industry/Entity Type

Plumbing

Colors
0054AA
0677BA
7BADD7
CADEEF
E8F1F8

Requirements
Must have
• Services we off and our logo, also must say "local plumber"

```html
<!DOCTYPE html>
<html lang="en">
<head>
<meta charset="utf-8">
<title>Plumbing Flyer</title>
<link rel="stylesheet" href="https://fonts.googleapis.com/css2?family=Archivo:wght@600;700;800&family=Big+Shoulders+Display:wght@800&display=swap">
<style>
  :root {
    --navy: #1b2a5c;
    --sky: #29a8e0;
    --paper: #ffffff;
    --backdrop: #636d72;
    --tint-a: #e8f1f8;
    --tint-b: #cadeef;
  }
  * { margin: 0; padding: 0; box-sizing: border-box; }
  html, body { width: 1200px; height: 1200px; overflow: hidden; }
  body { background: var(--backdrop); position: relative; font-family: "Archivo", sans-serif; color: var(--navy); }

  .flyer { position: absolute; left: 191px; top: 309px; width: 818px; height: 581px; background: var(--paper); overflow: hidden; }

  .footer-band { position: absolute; inset: 0; width: 818px; height: 581px; }

  .plumber-figure { position: absolute; left: 0; top: 20px; width: 205px; height: 561px;
    background: linear-gradient(180deg, var(--tint-a) 0%, var(--tint-b) 100%); border-radius: 6px 6px 0 0; z-index: 2; }

  .headline { position: absolute; left: 232px; top: 38px; font-family: "Big Shoulders Display", sans-serif; font-weight: 800; line-height: 1; color: var(--navy); white-space: nowrap; }
  .headline-lead { display: block; font-size: 58px; transform: scaleX(0.78); transform-origin: left center; }
  .headline-main { display: block; font-size: 101px; margin-top: -2px; transform: scaleX(0.9); transform-origin: left center; }

  .brand { position: absolute; left: 622px; top: 40px; width: 166px; text-align: center; }
  .brand-dot { width: 64px; height: 64px; border-radius: 50%; background: var(--navy); margin: 0 auto 10px; }
  .brand-name { font-family: "Big Shoulders Display", sans-serif; font-weight: 800; font-size: 30px; line-height: 1; letter-spacing: 2px; color: var(--navy); }

  .tagline { position: absolute; left: 225px; top: 229px; width: 565px; height: 39px; border: 2px solid var(--sky); border-radius: 20px;
    display: flex; align-items: center; padding-left: 14px; font-weight: 700; font-size: 18.5px; letter-spacing: 0.1px; white-space: nowrap; }

  .services { position: absolute; left: 0; top: 0; list-style: none; }
  .service { position: absolute; top: 294px; width: 116px; margin-left: -58px; text-align: center; list-style: none; }
  .service-badge { width: 81px; height: 81px; margin: 0 auto; border-radius: 50%; border: 1.5px dashed var(--sky);
    display: flex; align-items: center; justify-content: center; }
  .service-badge svg { width: 72px; height: 72px; }
  .service-label { margin-top: 14px; font-weight: 600; font-size: 14.5px; line-height: 1.25; text-transform: uppercase; white-space: nowrap; }

  .call-line { position: absolute; left: 245px; top: 467px; display: flex; align-items: center; font-weight: 800; white-space: nowrap; }
  .call-prompt { font-size: 31px; letter-spacing: -0.3px; }
  .call-icon { width: 36px; height: 36px; margin: 0 14px 0 16px; }
  .call-number { font-size: 31px; letter-spacing: 0.3px; }

  .contact-row { position: absolute; left: 243px; top: 529px; display: flex; align-items: center; color: var(--paper); font-weight: 600; font-size: 14px; white-space: nowrap; }
  .contact-row svg { width: 22px; height: 18px; margin-right: 9px; }
  .contact-web { margin-left: 12px; display: flex; align-items: center; }
</style>
</head>
<body>
  <main class="flyer">
    <svg class="footer-band" viewBox="0 0 818 581" aria-hidden="true">
      <path fill="#1b2a5c" d="M0,459 L190,459 Q197,459 200,465 L220,514 Q223,520 230,520 L750,520 Q756,520 759,514 L779,465 Q782,459 789,459 L818,459 L818,581 L0,581 Z"/>
    </svg>

    <div class="plumber-figure" role="img" aria-label="Line illustration of a plumber in cap and overalls holding a pipe wrench"></div>

    <h1 class="headline">
      <span class="headline-lead">NEED A PROFESSIONAL</span>
      <span class="headline-main">PLUMBER?</span>
    </h1>

    <div class="brand">
      <div class="brand-dot"></div>
      <div class="brand-name">CLEARWATER PLUMBING</div>
    </div>

    <p class="tagline">QUALITY PLUMBING SERVICES THAT YOU CAN TRUST</p>

    <ul class="services">
      <li class="service" style="left:265px">
        <div class="service-badge"><svg viewBox="0 0 72 72"><circle cx="36" cy="36" r="36" fill="#1b2a5c"/><path fill="#fff" d="M37 16c2 8 12 13 12 24a13 13 0 0 1-26 0c0-6 4-10 6-13 1 4 3 6 5 7-1-7 1-13 3-18z"/><circle cx="36" cy="42" r="5" fill="#1b2a5c"/></svg></div>
        <p class="service-label">Hot water<br>issues</p>
      </li>
      <li class="service" style="left:383px">
        <div class="service-badge"><svg viewBox="0 0 72 72"><circle cx="36" cy="36" r="36" fill="#1b2a5c"/><path fill="#fff" d="M24 18h10v4h-2v12h14v-2h6v18h-6v-2H32a8 8 0 0 1-8-8V22h-2v-4z"/><path fill="#1b2a5c" d="M30 34l-3 5 3 1-2 5 4-6-3-1z"/><path fill="#fff" d="M29 48c2 3 3 4 3 6a3 3 0 0 1-6 0c0-2 1-3 3-6z"/></svg></div>
        <p class="service-label">Burst<br>pipes</p>
      </li>
      <li class="service" style="left:502px">
        <div class="service-badge"><svg viewBox="0 0 72 72"><circle cx="36" cy="36" r="36" fill="#1b2a5c"/><path fill="#fff" d="M44 17l10 10-5 5-3-3-4 4 2 2-18 18-5-5 18-18 2 2 4-4-4-4z"/></svg></div>
        <p class="service-label">Gas<br>plumbing</p>
      </li>
      <li class="service" style="left:621px">
        <div class="service-badge"><svg viewBox="0 0 72 72"><circle cx="36" cy="36" r="36" fill="#1b2a5c"/><path fill="none" stroke="#fff" stroke-width="4" d="M18 34l16-13 10 8M24 32v19h22V38M31 51V41h8v10"/><path fill="#fff" d="M50 22c3 4 4 6 4 8a4 4 0 0 1-8 0c0-2 1-4 4-8z"/></svg></div>
        <p class="service-label">Roof<br>leaks</p>
      </li>
      <li class="service" style="left:740px">
        <div class="service-badge"><svg viewBox="0 0 72 72"><circle cx="36" cy="36" r="36" fill="#1b2a5c"/><path fill="#fff" d="M24 16h12v4h-4v6h-4v-6h-4z"/><circle cx="40" cy="37" r="11" fill="#fff"/><circle cx="40" cy="37" r="7.5" fill="#1b2a5c"/><path stroke="#fff" stroke-width="2.5" d="M36 33l8 8M44 33l-8 8"/><path fill="#fff" d="M36 48h8v6h3v4H33v-4h3z"/></svg></div>
        <p class="service-label">Drain<br>blockages</p>
      </li>
    </ul>

    <div class="call-line">
      <span class="call-prompt">CALL US NOW</span>
      <svg class="call-icon" viewBox="0 0 36 36" aria-hidden="true"><path fill="#29a8e0" d="M8 4l6 7-3 4c2 4 5 7 9 9l4-3 7 6-4 5C15 32 4 21 4 9z"/><path fill="none" stroke="#29a8e0" stroke-width="2.5" stroke-linecap="round" d="M20 9a8 8 0 0 1 7 7M21 3a14 14 0 0 1 12 12"/></svg>
      <span class="call-number">0400 123 456</span>
    </div>

    <div class="contact-row">
      <svg viewBox="0 0 22 18" aria-hidden="true"><rect x="1" y="2" width="20" height="14" rx="1" fill="#fff"/><path d="M1 3l10 8 10-8" fill="none" stroke="#1b2a5c" stroke-width="1.5"/></svg>
      <span>info@clearwaterplumbing.com.au</span>
      <span class="contact-web">
        <svg viewBox="0 0 22 18" aria-hidden="true"><circle cx="11" cy="9" r="7.5" fill="none" stroke="#fff" stroke-width="1.6"/><ellipse cx="11" cy="9" rx="3.2" ry="7.5" fill="none" stroke="#fff" stroke-width="1.4"/><path d="M3.5 9h15M5 5h12M5 13h12" stroke="#fff" stroke-width="1.2"/></svg>
        <span>clearwaterplumbing.com.au</span>
      </span>
    </div>
  </main>
</body>
</html>
```